Larkmoor Forum Flyer to describe services

I provide data abstraction and consulting services to hospitals that are participating in an accreditation program for their bariatric surgery program. I need a flyer that I can hand out to potential clients that describes the services that I offer. I am attaching an info sheet that has the information on the services I offer. (One exception is that I no longer offer the remote dietitian services listed on the flyer) . I am also including a file with my logo. I would like this flyer to hand out at conferences where I meet people that might not be familiar with my business or who are not knowledgeable of how my services might benefit them. The most important service that I offer is the data abstraction subcontracting. I will provide a PPT that will provide further info on this service.

Target Market(s)

Bariatric program directors and surgeons

Industry/Entity Type

Healthcare

Font styles to use
Serif
Sans Serif

Colors

Designer to choose colors to be used in the design.

Requirements
Must have
• a description of the services I offer
• how subcontracting will benefit them and save them money
• something noting my experience as I am one of the most experienced professionals in this field of bariatric surgery accreditation
Nice to have
• I am not a designer and created the flyer that I have provided. I realize it is not very professional and would like something that looks fresh and professional.
Should not have
• I don't want it to be too wordy and yet it needs to have a description of services offered. I want to include the yellow in my logo, but the flyer sample I have given you has waaaaay too much yellow and want to tone that down!

```html
<!DOCTYPE html>
<html lang="en">
<head>
<meta charset="utf-8">
<title>Whitfield Consulting – Services Flyer</title>
<link rel="stylesheet" href="https://fonts.googleapis.com/css2?family=Montserrat:wght@600;700;800&family=Source+Sans+3:ital,wght@0,400;0,600;1,600&display=swap">
<style>
  :root {
    --ink: #1d1d1d;
    --charcoal: #161515;
    --yellow: #ffd900;
    --page: #ffffff;
    --backdrop: #dcdcdc;
    --photo-light: #d9d9d9;
    --photo-dark: #5c5c5c;
  }
  * { box-sizing: border-box; margin: 0; padding: 0; }
  html, body { width: 1200px; height: 1200px; overflow: hidden; }
  body {
    background: var(--backdrop);
    font-family: "Source Sans 3", "Helvetica Neue", Arial, sans-serif;
    color: var(--ink);
  }
  .flyer {
    position: absolute;
    left: 150px; top: 20px;
    width: 900px; height: 1160px;
    background: var(--page);
    overflow: hidden;
  }

  /* Header */
  .masthead {
    height: 118px;
    display: flex; align-items: center; justify-content: center; gap: 14px;
  }
  .brand-mark { width: 26px; height: 26px; background: var(--yellow); }
  .brand-name {
    font-family: "Montserrat", Arial, sans-serif;
    font-weight: 800; font-size: 34px; letter-spacing: -0.5px;
    color: var(--ink);
  }

  /* Hero */
  .hero {
    position: relative; height: 267px;
    background: radial-gradient(ellipse at 65% 60%, #4a3f3a 0%, #2a2422 45%, #141212 100%);
    display: flex; flex-direction: column; align-items: center; justify-content: center;
  }
  .hero h1 {
    font-family: "Montserrat", Arial, sans-serif;
    font-weight: 700; font-size: 55px; line-height: 68px;
    letter-spacing: 2px; color: #fff; text-align: center;
  }
  .hero .experience {
    margin-top: 14px;
    font-size: 16px; font-weight: 600; letter-spacing: 0.5px;
    color: var(--yellow); text-align: center;
  }
  .accent-rule { height: 8px; background: var(--yellow); }

  /* Content */
  .content { display: flex; height: 673px; }
  .services { width: 545px; padding: 30px 30px 0 32px; }
  .service { margin-bottom: 18px; }
  .service-head { display: flex; align-items: flex-start; gap: 13px; margin-bottom: 6px; }
  .service-icon {
    flex: none; width: 24px; height: 22px; border-radius: 5px;
    background: var(--yellow); border: 1.5px solid var(--ink);
    display: flex; align-items: center; justify-content: center;
  }
  .service-head h2 {
    font-family: "Montserrat", Arial, sans-serif;
    font-weight: 800; font-size: 16.5px; line-height: 21px; text-transform: uppercase;
  }
  .service p {
    font-size: 12.2px; line-height: 16.4px; text-transform: uppercase;
    text-align: justify; color: #222;
  }
  .service p + p { margin-top: 4px; }

  .profile { width: 355px; display: flex; flex-direction: column; }
  .portrait {
    height: 340px;
    background: linear-gradient(160deg, var(--photo-light) 0%, #b5b5b5 45%, var(--photo-dark) 100%);
  }
  .standard-box {
    flex: 1; background: var(--yellow);
    padding: 20px 36px 0 34px;
  }
  .standard-box h3 {
    font-family: "Montserrat", Arial, sans-serif;
    font-weight: 700; font-size: 14.5px; margin-bottom: 4px;
  }
  .standard-box .lead { font-style: italic; font-weight: 600; font-size: 13px; margin-bottom: 6px; }
  .standard-box ul { list-style: none; }
  .standard-box li {
    font-size: 13.4px; line-height: 17.5px; text-align: justify; margin-bottom: 9px;
  }
  .standard-box li svg { vertical-align: 1px; margin-right: 3px; }

  /* Footer */
  .contact-bar {
    position: absolute; left: 0; bottom: 0; width: 900px; height: 94px;
    background: var(--charcoal); color: #fff;
    display: flex; align-items: center; padding: 0 34px 0 32px; gap: 20px;
  }
  .contact-name { font-family: "Montserrat", Arial, sans-serif; font-weight: 800; font-size: 14.5px; }
  .contact-role { font-size: 14px; }
  .contact-person { margin-right: 8px; }
  .contact-item {
    display: flex; align-items: center; gap: 8px;
    font-family: "Montserrat", Arial, sans-serif; font-weight: 700; font-size: 11.5px;
  }
</style>
</head>
<body>
<main class="flyer">
  <header class="masthead">
    <span class="brand-mark"></span>
    <span class="brand-name">WHITFIELD CONSULTING</span>
  </header>

  <section class="hero" role="img" aria-label="Dim photo of a speaker addressing a conference audience">
    <h1>HELPING YOU NAVIGATE<br>MBSAQIP</h1>
    <p class="experience">Over 20 years of bariatric accreditation experience</p>
  </section>
  <div class="accent-rule"></div>

  <div class="content">
    <section class="services">
      <article class="service">
        <div class="service-head">
          <span class="service-icon"><svg width="8" height="14" viewBox="0 0 8 14"><circle cx="4" cy="2" r="1.8" fill="#1d1d1d"/><rect x="2" y="5" width="4" height="8" fill="#1d1d1d"/></svg></span>
          <h2>Program Assessment:</h2>
        </div>
        <p>A 2-day on-site assessment of your bariatric program as it relates to MBSAQIP compliance, best practice, business strategies and evaluation of the process for collecting outcomes data. A comprehensive post-assessment review and written report will provide guidance, solutions, timelines and suggest opportunities for improvement.</p>
      </article>

      <article class="service">
        <div class="service-head">
          <span class="service-icon"><svg width="14" height="14" viewBox="0 0 14 14"><path d="M3 8V6a4 4 0 0 1 8 0v2" fill="none" stroke="#1d1d1d" stroke-width="1.5"/><rect x="2" y="7" width="2.5" height="4" fill="#1d1d1d"/><rect x="9.5" y="7" width="2.5" height="4" fill="#1d1d1d"/></svg></span>
          <h2>Program Development— Remote Assistance and On-Site:</h2>
        </div>
        <p>For centers currently developing a new program, assistance by experienced professionals can help to ensure accreditation and provide guidance in the development of policies and procedures, job descriptions, clinical pathways and protocols that will enhance program.</p>
        <p>As well as ensure MBSAQIP compliance. With the remote option consultant will meet with staff during regularly scheduled webinars.</p>
      </article>

      <article class="service">
        <div class="service-head">
          <span class="service-icon"><svg width="14" height="12" viewBox="0 0 14 12"><circle cx="4.5" cy="3" r="2.2" fill="#1d1d1d"/><circle cx="9.5" cy="3" r="2.2" fill="#1d1d1d"/><path d="M1 11a3.5 3.5 0 0 1 7 0zM6 11a3.5 3.5 0 0 1 7 0z" fill="#1d1d1d"/></svg></span>
          <h2>MBSCR Staffing:</h2>
        </div>
        <p>Maintain compliance with MBSAQIP data abstraction with a data abstractor who will be a member of your team, provide leadership and direction in the development of QI projects, perform routine quality assurance audits on data and attend all bariatric team meetings.</p>
      </article>

      <article class="service">
        <div class="service-head">
          <span class="service-icon"><svg width="14" height="14" viewBox="0 0 14 14"><circle cx="7" cy="7" r="4" fill="none" stroke="#1d1d1d" stroke-width="1.5"/><path d="M7 1v2M7 11v2M1 7h2M11 7h2" stroke="#1d1d1d" stroke-width="1.5"/></svg></span>
          <h2>Mock Site Inspections:</h2>
        </div>
        <p>This one-day rigorous evaluation of a facility evaluates accreditation readiness by providing a critical assessment of all areas related to the standards for MBSAQIP accreditation. It closely mirrors the MBSAQIP site survey process.</p>
      </article>

      <article class="service">
        <div class="service-head">
          <span class="service-icon"><svg width="14" height="14" viewBox="0 0 14 14"><circle cx="7" cy="7" r="5.3" fill="none" stroke="#1d1d1d" stroke-width="1.5"/><path d="M7 3.5v7M8.8 5.2C8.3 4.5 5.2 4.3 5.2 5.8s3.6 1 3.6 2.6-3.1 1.3-3.8.5" fill="none" stroke="#1d1d1d" stroke-width="1.2"/></svg></span>
          <h2>Why Subcontract?</h2>
        </div>
        <p>Subcontracting your MBSCR saves the cost of a full-time salary, benefits, training and turnover. You pay only for the abstraction you need, with no gaps in coverage and data entered by a certified, highly experienced professional.</p>
      </article>
    </section>

    <aside class="profile">
      <div class="portrait" role="img" aria-label="Black and white portrait photo of the consultant"></div>
      <div class="standard-box">
        <h3>Why do we need MBSCR?</h3>
        <p class="lead">The Standard states:</p>
        <ul>
          <li><svg width="9" height="8" viewBox="0 0 9 8"><path d="M1 4.5l2.3 2.3L8 1" fill="none" stroke="#1d1d1d" stroke-width="1.6"/></svg>Each center is required to provide an MBSCR to enter data into the MBSAQIP registry.</li>
          <li><svg width="9" height="8" viewBox="0 0 9 8"><path d="M1 4.5l2.3 2.3L8 1" fill="none" stroke="#1d1d1d" stroke-width="1.6"/></svg>MBSCR should not be supervising patient care.</li>
          <li><svg width="9" height="8" viewBox="0 0 9 8"><path d="M1 4.5l2.3 2.3L8 1" fill="none" stroke="#1d1d1d" stroke-width="1.6"/></svg>Must be able to fulfill case abstraction duties.</li>
          <li><svg width="9" height="8" viewBox="0 0 9 8"><path d="M1 4.5l2.3 2.3L8 1" fill="none" stroke="#1d1d1d" stroke-width="1.6"/></svg>Must be able to complete ongoing training and recertification requirements.</li>
          <li><svg width="9" height="8" viewBox="0 0 9 8"><path d="M1 4.5l2.3 2.3L8 1" fill="none" stroke="#1d1d1d" stroke-width="1.6"/></svg>Must be able to retrieve and enter long-term follow-up data on a compounding number of patients over time.</li>
          <li><svg width="9" height="8" viewBox="0 0 9 8"><path d="M1 4.5l2.3 2.3L8 1" fill="none" stroke="#1d1d1d" stroke-width="1.6"/></svg>Must be able to fulfill requests for patient data and reports.</li>
        </ul>
      </div>
    </aside>
  </div>

  <footer class="contact-bar">
    <div class="contact-person">
      <div class="contact-name">Dana Whitfield, RN, CBN</div>
      <div class="contact-role">Bariatric Program Consultant</div>
    </div>
    <div class="contact-item">
      <svg width="11" height="18" viewBox="0 0 11 18"><rect x="1" y="1" width="9" height="16" rx="2" fill="none" stroke="#fff" stroke-width="1.5"/><circle cx="5.5" cy="14" r="1" fill="#fff"/></svg>
      555-014-2290
    </div>
    <div class="contact-item">
      <svg width="22" height="15" viewBox="0 0 22 15"><rect width="22" height="15" fill="#fff"/><path d="M0 0l11 8 11-8" fill="none" stroke="#161515" stroke-width="1.6"/></svg>
      dana@whitfieldconsulting.example
    </div>
    <div class="contact-item">
      <svg width="22" height="20" viewBox="0 0 22 20"><rect x="1" y="3" width="16" height="11" rx="1" fill="none" stroke="#fff" stroke-width="1.4"/><path d="M6 18h6M9 14v4" stroke="#fff" stroke-width="1.4"/><circle cx="16" cy="6" r="5" fill="#161515" stroke="#fff" stroke-width="1.3"/><path d="M11 6h10M16 1v10" stroke="#fff" stroke-width="1"/></svg>
      whitfieldconsulting.example
    </div>
  </footer>
</main>
</body>
</html>
```